Letterhead and matching envelope design for a dental office

We need a new stationary design, letterhead and envelope #10, for a dental office in Denver area. We are called Brightfield Dental. We want a simple and minimalistic design but not a boring design. I wish to have one good point that makes it look professional. I have attached our logo. Feel free to use either one. I want the design for letterhead and envelope look like a "matching pair" but not look the same. The envelope doesn't have to be white and it will have an address window on bottom left.

Target Market(s)

everyone who visits dentist (adults)

Industry/Entity Type

Dental

Font styles to use
Other font styles liked:
• close to font on logo or something that matches well

Requirements
Must have
• professional
• simple, minimalistic
• unique point that stands out
Nice to have
• matching but not same design for letterhead and envelope
Should not have
• not look like all the other boring designs
• no flowery, distracting feats

```html
<!DOCTYPE html>
<html lang="en">
<head>
<meta charset="utf-8">
<title>Brightfield Dental Stationery</title>
<link href="https://fonts.googleapis.com/css2?family=Cinzel:wght@700&family=Montserrat:wght@300;400;600&display=swap" rel="stylesheet">
<style>
  :root {
    --brand-green: #45b649;
    --paper: #ffffff;
    --backdrop: #d1d2d4;
  }
  * { margin: 0; padding: 0; box-sizing: border-box; }
  html, body { width: 1200px; height: 927px; overflow: hidden; }
  body { background: var(--backdrop); position: relative; font-family: "Montserrat", sans-serif; }

  .sheet { position: absolute; overflow: hidden; }
  .wordmark {
    font-family: "Cinzel", serif; font-weight: 700; color: var(--brand-green);
    letter-spacing: 1px; white-space: nowrap;
  }
  .tagline {
    font-family: "Cinzel", serif; font-weight: 700; color: var(--brand-green);
    letter-spacing: 6px; white-space: nowrap;
  }

  /* Letterhead */
  .letterhead { left: 170px; top: 60px; width: 421px; height: 543px; background: var(--paper); }
  .letterhead .brand { position: absolute; left: 20px; top: 70px; width: 175px; text-align: center; }
  .letterhead .wordmark { font-size: 12.5px; }
  .letterhead .tagline { font-size: 5.5px; margin-top: 2px; }
  .letterhead .contact {
    position: absolute; right: 18px; top: 42px; text-align: right;
    color: var(--brand-green); font-size: 9.5px; line-height: 12px;
  }
  .letterhead .contact .gap { height: 5px; }
  .letterhead .contact svg { width: 7px; height: 7px; margin-left: 4px; vertical-align: -1px; }
  .letterhead .rule { position: absolute; left: 19px; right: 18px; top: 98px; height: 1.5px; background: var(--brand-green); }
  .letterhead .foot-band { position: absolute; left: 0; right: 0; bottom: 0; height: 17px; background: var(--brand-green); }

  /* Folder */
  .folder { left: 621px; top: 60px; width: 421px; height: 543px; background: var(--brand-green); }
  .folder .foot-band { position: absolute; left: 0; right: 0; bottom: 0; height: 17px; background: var(--paper); }
  .folder .brand { position: absolute; left: 0; right: 0; top: 238px; text-align: center; }
  .brand-dot { display: inline-block; border-radius: 50%; background: var(--paper); }
  .folder .brand-dot { width: 22px; height: 22px; margin-bottom: 12px; }
  .folder .wordmark { color: var(--paper); font-size: 24px; letter-spacing: 3px; }
  .folder .address { position: absolute; left: 0; right: 0; top: 508px; text-align: center; color: var(--paper); font-size: 9.5px; }

  /* Envelope, white face */
  .envelope-front { left: 129px; top: 638px; width: 460px; height: 229px; background: var(--paper); border-radius: 12px 12px 0 0; }
  .envelope-front .flap-band { position: absolute; left: 0; right: 0; top: 0; height: 22px; background: var(--brand-green); }
  .envelope-front .foot-band { position: absolute; left: 0; right: 0; bottom: 0; height: 18px; background: var(--brand-green); }
  .envelope-front .brand { position: absolute; left: 0; right: 0; top: 133px; text-align: center; }
  .envelope-front .wordmark { font-size: 15px; letter-spacing: 1.5px; }
  .envelope-front .tagline { font-size: 6.5px; letter-spacing: 8px; margin-top: 1px; }
  .envelope-front .address { position: absolute; left: 0; right: 0; top: 185px; text-align: center; color: var(--brand-green); font-size: 17.5px; font-weight: 400; }

  /* Envelope, green back */
  .envelope-back { left: 614px; top: 660px; width: 458px; height: 207px; background: var(--brand-green); }
  .envelope-back .flap-band { position: absolute; left: 0; right: 0; top: 0; height: 22px; background: var(--paper); border-radius: 0 0 12px 12px; }
  .envelope-back .brand { position: absolute; left: 0; right: 0; top: 92px; text-align: center; }
  .envelope-back .brand-dot { width: 14px; height: 14px; margin-bottom: 7px; }
  .envelope-back .wordmark { color: var(--paper); font-size: 14px; letter-spacing: 2px; }
</style>
</head>
<body>

<section class="sheet letterhead" aria-label="Letterhead">
  <div class="brand">
    <div class="wordmark">Brightfield Dental</div>
    <div class="tagline">Lakewood</div>
  </div>
  <address class="contact" style="font-style:normal">
    <div>PO BOX 4120</div>
    <div>Lakewood CO 80226</div>
    <div class="gap"></div>
    <div>+1 303 555-0148<svg viewBox="0 0 10 10" aria-hidden="true"><path d="M2 1l2 2-1 1.2c.6 1.2 1.6 2.2 2.8 2.8L7 6l2 2-1.2 1.5C4.5 9.3.7 5.5.5 2.2z" fill="#45b649"/></svg></div>
    <div>info@<b style="font-weight:600">brightfielddental</b>.com<svg viewBox="0 0 10 10" aria-hidden="true"><rect x="0.7" y="2" width="8.6" height="6" fill="none" stroke="#45b649" stroke-width="1.2"/><path d="M1 2.5l4 3 4-3" fill="none" stroke="#45b649" stroke-width="1.2"/></svg></div>
  </address>
  <div class="rule"></div>
  <div class="foot-band"></div>
</section>

<section class="sheet folder" aria-label="Presentation folder">
  <div class="brand">
    <span class="brand-dot"></span>
    <div class="wordmark">Brightfield Dental</div>
  </div>
  <div class="address">PO BOX 4120 Lakewood CO 80226</div>
  <div class="foot-band"></div>
</section>

<section class="sheet envelope-front" aria-label="Envelope front">
  <div class="flap-band"></div>
  <div class="brand">
    <div class="wordmark">Brightfield Dental</div>
    <div class="tagline">Lakewood</div>
  </div>
  <div class="address">PO BOX 4120 Lakewood CO 80226</div>
  <div class="foot-band"></div>
</section>

<section class="sheet envelope-back" aria-label="Envelope back">
  <div class="flap-band"></div>
  <div class="brand">
    <span class="brand-dot"></span>
    <div class="wordmark">Brightfield Dental</div>
  </div>
</section>

</body>
</html>
```